Vireo M.K. - Diagnostic Ultrasound Flyer

About US
Vireo M.K. is a concierge ultrasound company that provides onsite or offsite diagnostic ultrasounds. We have over 14 years experience in sonography, business management, and customer service. We offer both the physician and patient flexibility, convenience, and access to timely services.

We provide ultrasounds for the following specialties:
Obstetrics/Gynecology
Abdominal
Small Parts
Vascular

Company Features:
1. Onsite or Offsite Scans
2. Images Available Immediately for Referring Physician and Patient
3. Flexible Options for Ultrasound Interpretation/Billing
4. Access to Interpreting Radiologist
5. Final Report Process - 1-2 Business Days/ 1 hour for STAT.
6. PACS Storage with Secure Access.

We need a place to add in our contact information (address, email, website, phone)

We already have a logo and would like to use it ( they are attached). We would the colors to match the logo colors....maybe lighter version of yellow and blue.

```html
<!DOCTYPE html>
<html lang="en">
<head>
<meta charset="utf-8">
<title>Vireo M.K. – Diagnostic Ultrasound Flyer</title>
<link href="https://fonts.googleapis.com/css2?family=Crimson+Pro:wght@700&family=Roboto:wght@400;500;700;900&display=swap" rel="stylesheet">
<style>
  :root{
    --indigo:#1d1480;
    --violet:#3a2d9c;
    --gold:#fdc02f;
    --cream:#fde08f;
    --ink:#1b1b2e;
    --paper:#ffffff;
    --paper-shade:#f1f1f1;
    --backdrop:#e4e4e6;
  }
  *{margin:0;padding:0;box-sizing:border-box}
  html,body{width:990px;height:1200px;overflow:hidden;background:var(--backdrop)}
  body{font-family:"Roboto",Arial,sans-serif;color:var(--ink)}
  .flyer{position:absolute;left:31px;top:0;width:928px;height:1200px;overflow:hidden;
    background:linear-gradient(180deg,var(--paper) 0%,var(--paper-shade) 100%)}
  .shapes{position:absolute;left:0;top:0}
  .brand{position:absolute;left:82px;top:66px;font-family:"Roboto",Arial,sans-serif;font-weight:900;
    font-size:54px;letter-spacing:2px;color:var(--indigo);line-height:1}
  .photo{position:absolute;left:457px;top:72px;width:568px;height:568px;border-radius:50%;
    background:radial-gradient(circle at 45% 40%,#9b6a55 0%,#c99fa0 35%,#eadbd6 65%,#d9d2cf 100%)}
  .title{position:absolute;left:0;top:218px;width:482px;text-align:center;
    font-family:"Crimson Pro",Georgia,serif;font-weight:700;font-size:74px;line-height:66px}
  .title .white{color:#fff}
  .title .gold{color:var(--gold)}
  .about-tag{position:absolute;left:82px;top:472px;height:41px;padding:0 18px 0 16px;
    background:var(--gold);border-left:5px solid #fff;color:var(--indigo);font-weight:700;
    font-size:26px;line-height:41px}
  .about-text{position:absolute;left:82px;top:526px;color:#fff;font-size:17.6px;line-height:21.8px;white-space:nowrap}
  .specialties-head{position:absolute;left:82px;top:797px;color:var(--violet);font-weight:700;font-size:26px;line-height:34px}
  .specialties-rule{position:absolute;left:82px;top:876px;width:286px;height:3px;background:var(--gold)}
  .specialties{position:absolute;left:76px;top:896px;list-style:none}
  .specialties li{display:flex;align-items:center;height:41.5px;font-weight:500;font-size:20.5px;color:var(--ink)}
  .specialties svg{margin-right:16px}
  .features{position:absolute;left:474px;top:705px;width:371px;height:351px;background:var(--gold);border-radius:0 18px 0 18px}
  .features-head{position:absolute;left:513px;top:684px;width:297px;height:40px;background:var(--violet);
    color:var(--gold);font-weight:500;font-size:26px;line-height:40px;text-align:center}
  .feature-list{position:absolute;left:508px;top:738px;width:294px;list-style:none}
  .feature-list li{font-weight:500;font-size:17.4px;line-height:22px;color:var(--ink);
    padding:5px 0 6px;border-bottom:1px solid var(--ink)}
  .feature-list li:last-child{border-bottom:none}
  .address{position:absolute;left:82px;top:1109px;font-weight:500;font-size:17px;line-height:22px;color:var(--ink)}
  .address-pin{position:absolute;left:60px;top:1110px}
  .phone{position:absolute;left:474px;top:1079px;width:371px;height:47px;border-radius:24px;background:#fff}
  .phone-icon{position:absolute;left:472px;top:1074px}
  .phone-number{position:absolute;left:547px;top:1079px;font-weight:700;font-size:36px;line-height:47px;color:var(--violet)}
  .contact{position:absolute;top:1140px;font-weight:500;font-size:17px;line-height:22px;color:var(--gold);display:flex;align-items:center;gap:6px}
  .contact.email{left:482px}
  .contact.web{left:687px}
</style>
</head>
<body>
<main class="flyer">
  <svg class="shapes" width="928" height="1200" viewBox="0 0 928 1200" aria-hidden="true">
    <circle cx="741" cy="356" r="305" fill="var(--cream)"/>
    <circle cx="212" cy="466" r="302" fill="var(--violet)"/>
    <circle cx="198" cy="491" r="265" fill="var(--indigo)"/>
    <rect x="0" y="1093" width="460" height="75" fill="var(--gold)"/>
    <path d="M382 1200 C420 1060 560 990 720 995 C820 998 890 1040 927 1083 L928 1200 Z" fill="var(--violet)"/>
  </svg>

  <div class="brand">Vireo M.K.</div>

  <div class="photo" role="img" aria-label="Photo of a smiling expectant mother lying on an exam bed beside her partner during an ultrasound scan" style="width:568px;height:568px;left:457px;top:72px"></div>

  <h1 class="title"><span class="white">Diagnostic</span><br><span class="gold">Medical<br>Ultrasound</span></h1>

  <div class="about-tag">ABOUT US</div>
  <p class="about-text">Vireo M.K. is a concierge ultrasound<br>company that provides onsite or offsite<br>diagnostic ultrasounds. We have over<br>14 years experience in sonography,<br>business management, and customer<br>service. We offer both the physician<br>and patient flexibility, convenience, and<br>access to timely services.</p>

  <h2 class="specialties-head">We provide ultrasounds<br>for the following specialties:</h2>
  <div class="specialties-rule"></div>
  <ul class="specialties">
    <li><svg width="28" height="28" viewBox="0 0 28 28" aria-hidden="true"><circle cx="14" cy="14" r="13" fill="var(--violet)" stroke="var(--gold)" stroke-width="2.5"/><path d="M8.5 14.5l3.8 3.6 7.2-7.6" fill="none" stroke="var(--gold)" stroke-width="2.4" stroke-linecap="round" stroke-linejoin="round"/></svg>OBSTETRICS/GYNECOLOGY</li>
    <li><svg width="28" height="28" viewBox="0 0 28 28" aria-hidden="true"><circle cx="14" cy="14" r="13" fill="var(--violet)" stroke="var(--gold)" stroke-width="2.5"/><path d="M8.5 14.5l3.8 3.6 7.2-7.6" fill="none" stroke="var(--gold)" stroke-width="2.4" stroke-linecap="round" stroke-linejoin="round"/></svg>ABDOMINAL</li>
    <li><svg width="28" height="28" viewBox="0 0 28 28" aria-hidden="true"><circle cx="14" cy="14" r="13" fill="var(--violet)" stroke="var(--gold)" stroke-width="2.5"/><path d="M8.5 14.5l3.8 3.6 7.2-7.6" fill="none" stroke="var(--gold)" stroke-width="2.4" stroke-linecap="round" stroke-linejoin="round"/></svg>SMALL PARTS</li>
    <li><svg width="28" height="28" viewBox="0 0 28 28" aria-hidden="true"><circle cx="14" cy="14" r="13" fill="var(--violet)" stroke="var(--gold)" stroke-width="2.5"/><path d="M8.5 14.5l3.8 3.6 7.2-7.6" fill="none" stroke="var(--gold)" stroke-width="2.4" stroke-linecap="round" stroke-linejoin="round"/></svg>VASCULAR</li>
  </ul>

  <div class="features"></div>
  <h2 class="features-head">Company Features:</h2>
  <ol class="feature-list">
    <li>1. Onsite or Offsite Scans</li>
    <li>2. Images Available Immediately<br>for Referring Physician and Patient</li>
    <li>3. Flexible Options for<br>Ultrasound Interpretation/Billing</li>
    <li>4. Access to Interpreting Radiologist</li>
    <li>5. Final Report Process -<br>1-2 Business Days/ 1 hour for STAT.</li>
    <li>6. PACS Storage with Secure Access.</li>
  </ol>

  <svg class="address-pin" width="14" height="20" viewBox="0 0 14 20" aria-hidden="true"><circle cx="7" cy="6" r="4.5" fill="none" stroke="var(--ink)" stroke-width="1.6"/><path d="M7 10.5V18M3 18h8" stroke="var(--ink)" stroke-width="1.6" fill="none" stroke-linecap="round"/></svg>
  <p class="address">2140 Linden Park Road Suite B4<br>Fairhaven, MD 20814, USA</p>

  <div class="phone"></div>
  <svg class="phone-icon" width="56" height="56" viewBox="0 0 56 56" aria-hidden="true"><circle cx="28" cy="28" r="27" fill="var(--gold)"/><circle cx="28" cy="28" r="20" fill="none" stroke="var(--violet)" stroke-width="2.5"/><path d="M22 19c1.5-1 3 .3 3.8 2.2.7 1.6-.6 2.6-1.3 3.2.9 2.4 2.6 4.3 4.9 5.4.6-.7 1.6-2 3.2-1.3 1.9.8 3.1 2.4 2.1 3.9-1.5 2.1-4.3 2.3-7.6.2-3.9-2.5-6.6-6.8-6.8-10.3-.1-1.5.4-2.6 1.7-3.3z" fill="var(--violet)"/></svg>
  <div class="phone-number">(410) 555-0186</div>

  <div class="contact email"><svg width="18" height="14" viewBox="0 0 18 14" aria-hidden="true"><rect x="1" y="1" width="16" height="12" fill="none" stroke="#fff" stroke-width="1.4"/><path d="M1 1l8 6.5L17 1M1 13l6-5.5M17 13l-6-5.5" fill="none" stroke="#fff" stroke-width="1.4"/></svg>info@vireo-mk.com</div>
  <div class="contact web"><svg width="16" height="16" viewBox="0 0 16 16" aria-hidden="true"><circle cx="8" cy="8" r="7" fill="none" stroke="#fff" stroke-width="1.3"/><ellipse cx="8" cy="8" rx="3" ry="7" fill="none" stroke="#fff" stroke-width="1.2"/><path d="M1 8h14M2.5 4.5h11M2.5 11.5h11" stroke="#fff" stroke-width="1.1"/></svg>www.vireo-mk.com</div>
</main>
</body>
</html>
```